Varlowe Supply Partners
Business Cards and Stationary
Project: Varlowe Supply Partners
Varlowe Supply Partners -
Creative Brief
Professional
Daniel Varlowe
Manufacturer's Representative
20375 82nd Lane NW Elk Ridge, MN 55492
dvarlowe@varlowesupply-example.com
www.varlowesupply-example.com

```html
<!DOCTYPE html>
<html lang="en">
<head>
<meta charset="utf-8">
<title>Varlowe Supply Partners – Business Cards</title>
<link href="https://fonts.googleapis.com/css2?family=Arimo:wght@400;700&display=swap" rel="stylesheet">
<style>
  :root {
    --page: #e6e8eb;
    --card: #ffffff;
    --navy: #1f4f8f;
    --blue: #1d5aa6;
    --ink: #4a5566;
    --faint: #dfe6f1;
    --pale: #c9d6ea;
  }
  html, body {
    margin: 0;
    width: 1200px;
    height: 901px;
    overflow: hidden;
    background: var(--page);
  }
  .canvas { position: relative; width: 1200px; height: 901px; }
  .card {
    position: absolute;
    background: var(--card);
    border-radius: 14px;
    overflow: hidden;
  }
  .card--front { left: 29px; top: 15px; width: 615px; height: 425px; }
  .card--back  { left: 574px; top: 460px; width: 584px; height: 436px; }

  .brand { position: absolute; display: flex; align-items: center; }
  .brand__dot { border-radius: 50%; background: var(--navy); flex: none; }
  .brand__name {
    font-family: "Arimo", sans-serif;
    font-weight: 400;
    color: var(--navy);
    line-height: 1;
    white-space: nowrap;
  }

  .card--front .brand { left: 98px; top: 96px; }
  .card--front .brand__dot { width: 54px; height: 54px; margin-right: 10px; }
  .card--front .brand__name { font-size: 21px; }

  .side-bar { position: absolute; left: 0; top: 163px; width: 56px; height: 175px; background: var(--blue); }
  .faint-disc { position: absolute; border-radius: 50%; background: var(--faint); }
  .card--front .faint-disc { left: 388px; top: 190px; width: 225px; height: 240px; }

  .contact {
    position: absolute; left: 80px; top: 184px;
    font-family: "Arimo", sans-serif; font-size: 12px; color: var(--ink);
    border-collapse: collapse;
  }
  .contact th {
    text-align: left; font-weight: 700; color: var(--navy);
    width: 98px; padding: 0; vertical-align: top; white-space: nowrap;
  }
  .contact td { padding: 0; line-height: 1.3; white-space: nowrap; }
  .contact tr + tr th, .contact tr + tr td { padding-top: 13px; }

  .card--back .faint-disc { left: -30px; top: 30px; width: 300px; height: 340px; }
  .card--back .brand { left: 88px; top: 176px; }
  .card--back .brand__dot { width: 98px; height: 98px; margin-right: 10px; }
  .card--back .brand__name { font-size: 28px; }
  .swoosh { position: absolute; left: 0; top: 0; }
  .web {
    position: absolute; left: 27px; top: 395px;
    font-family: "Arimo", sans-serif; font-size: 15px; color: var(--navy);
  }
</style>
</head>
<body>
<main class="canvas">
  <section class="card card--front" aria-label="Business card front with contact details">
    <div class="faint-disc"></div>
    <div class="brand">
      <span class="brand__dot"></span>
      <span class="brand__name">Varlowe Supply Partners</span>
    </div>
    <div class="side-bar"></div>
    <table class="contact">
      <tr><th>ADDRESS</th><td>20375 82nd Lane NW<br>Elk Ridge, MN 55492</td></tr>
      <tr><th>PHONE</th><td>763.555.0142</td></tr>
      <tr><th>FAX</th><td>763.555.0178</td></tr>
      <tr><th>EMAIL</th><td>dvarlowe@varlowesupply-example.com</td></tr>
      <tr><th>WEB ADDRESS</th><td>www.varlowesupply-example.com</td></tr>
    </table>
  </section>

  <section class="card card--back" aria-label="Business card back with company name">
    <div class="faint-disc"></div>
    <svg class="swoosh" width="584" height="436" viewBox="0 0 584 436" aria-hidden="true">
      <path d="M330 436 C420 405 520 335 584 228 L584 436 Z" fill="var(--pale)"/>
      <path d="M352 436 C440 410 530 345 584 253 L584 436 Z" fill="var(--blue)"/>
    </svg>
    <div class="brand">
      <span class="brand__dot"></span>
      <span class="brand__name">Varlowe Supply Partners</span>
    </div>
    <div class="web">www.varlowesupply-example.com</div>
  </section>
</main>
</body>
</html>
```